Word template for proposals we send to clients

We want a word template designed based on the look/feel of our website. The website is www.brovexa.com.au and while we have pictures of 2 staff on the website we have pictures of other staff if required

the template will be used to send out proposals to potential clients, therefore it has to be professional, modern and compelling for someone to open

Target Market(s)

B2B

Industry/Entity Type

It Company

Font styles to use
Serif

Colors

Designer to choose colors to be used in the design.

Requirements
Must have
• Same look and feel as website
Nice to have
• Dont know what I am missing so anythign you feel i need to add

```html
<!DOCTYPE html>
<html lang="en">
<head>
<meta charset="utf-8">
<title>Brovexa Proposal Template</title>
<link href="https://fonts.googleapis.com/css2?family=Open+Sans:wght@400;600;700;800&display=swap" rel="stylesheet">
<style>
:root{
  --bg:#5c5c5c;
  --navy:#2e3748;
  --lime:#b3c02f;
  --olive:#7d9a3d;
  --paper:#ffffff;
  --ink:#3a3a3a;
  --bubble:#f3e27a;
}
*{box-sizing:border-box;margin:0;padding:0}
html,body{width:960px;height:1200px;overflow:hidden}
body{background:radial-gradient(circle at 50% 40%,#6a6a6a,#4a4a4a);font-family:"Open Sans",sans-serif;color:var(--ink);position:relative}
.page{position:absolute;width:393px;height:556px;background:var(--paper);overflow:hidden;box-shadow:0 2px 8px rgba(0,0,0,.35)}
.p-cover{left:66px;top:34px}
.p-about{left:496px;top:34px}
.p-services{left:66px;top:608px}
.p-values{left:496px;top:608px}
.abs{position:absolute}
.footer{position:absolute;left:0;right:0;bottom:0;height:60px;background:var(--olive);color:#fff;font-size:7px;line-height:1.45;display:flex;align-items:center;padding:0 20px;gap:28px}
.footer .item{display:flex;align-items:center;gap:8px}
.footer svg{width:8px;height:8px;fill:#fff;flex:none}
.p-about .footer,.p-services .footer{height:42px}

/* cover */
.cover-head{left:0;top:0;width:100%;height:90px;background:var(--navy);display:flex;align-items:center;justify-content:center}
.brand{color:var(--lime);font-weight:800;font-size:26px;letter-spacing:.5px;text-align:center}
.brand-sub{color:#fff;font-weight:700;font-size:9px;letter-spacing:2px;text-align:center;margin-top:-2px}
.intro{left:22px;top:136px;width:350px;height:100px;border:1px solid #b9b9b9;padding:20px 10px 0;text-align:center;font-size:7.4px;line-height:1.45;color:#333}
.intro h1{position:absolute;top:-12px;left:50%;transform:translateX(-50%);background:#fff;padding:0 8px;white-space:nowrap;color:var(--lime);font-size:19px;font-weight:600}
.cover-band{left:0;top:316px;width:100%;height:180px;background:var(--lime)}
.staff{position:absolute;border-radius:40px 40px 0 0}
.staff-a{left:14px;top:266px;width:150px;height:230px;background:linear-gradient(#8a6a55,#6f7fb0)}
.staff-b{left:230px;top:256px;width:140px;height:240px;background:linear-gradient(#c79a7a,#dfe6ee)}
.caption{position:absolute;font-size:5.5px;color:#333;text-align:center;line-height:1.2}
.caption b{display:block;font-size:6px}

/* about */
.about-side{left:8px;top:0;width:145px;height:514px;background:var(--lime)}
.about-title{left:8px;top:0;width:145px;height:92px;background:var(--navy);color:#fff;font-size:15px;font-weight:600;display:flex;align-items:center;justify-content:center}
.side-label{position:absolute;left:8px;width:145px;text-align:center;color:#fff;font-weight:600;font-size:12.5px}
.side-label svg{display:block;margin:0 auto 6px;width:20px;height:20px;fill:#fff;stroke:#fff}
.about-text{left:168px;width:214px;font-size:5.6px;line-height:1.5;text-align:justify;color:#444}
.rule{position:absolute;left:168px;width:214px;border-top:1px solid #ccc}

/* services */
.tab{position:absolute;left:51px;top:0;width:290px;height:32px;background:var(--navy);color:#fff;font-size:13px;font-weight:600;display:flex;align-items:center;justify-content:center;letter-spacing:.3px}
.svc-side{left:8px;top:40px;width:145px;height:474px;background:var(--lime)}
.svc-label{position:absolute;left:22px;width:125px;color:#fff;font-weight:700;font-size:12.5px;line-height:1.05}
.svc-text{position:absolute;left:168px;width:214px;font-size:5.5px;line-height:1.5;text-align:justify;color:#444}

/* values */
.values-art{left:8px;top:39px;width:378px;height:282px;background:linear-gradient(135deg,#c6d32e,#8aa63a 55%,#f2e35a)}
.values-bottom{left:0;top:320px;width:100%;height:236px;background:var(--olive)}
.tab-test{top:330px;height:22px;font-size:12px}
.bubble{position:absolute;background:var(--bubble);border:2px solid #2a2a2a;border-radius:50%;font-size:5.4px;line-height:1.45;text-align:center;display:flex;align-items:center;justify-content:center;padding:0 20px;color:#333}
.person{position:absolute;color:#fff;font-size:9px;line-height:1.25;white-space:nowrap}
.person b{font-weight:700}
</style>
</head>
<body>

<section class="page p-cover">
  <div class="abs cover-head">
    <div>
      <div class="brand">Brovexa</div>
      <div class="brand-sub">CONSULTING SERVICES</div>
    </div>
  </div>
  <div class="abs intro">
    <h1>IT SUPPORT + PERSONALITY</h1>
    Melbourne based IT Support that you can count on.<br>
    Every day small and medium businesses rely on Brovexa Consulting Services to keep their technology running smoothly. When you become a valued client of Brovexa you gain an IT partner who is on call 24/7. Whether we're creating a user, resolving performance issues, getting clients up-and-running after natural disasters or remediating ransomware, your IT support team is here for you.
  </div>
  <div class="abs cover-band"></div>
  <div class="staff staff-a" role="img" aria-label="Photo of Marco, support engineer, wearing a headset and holding a laptop"></div>
  <div class="staff staff-b" role="img" aria-label="Photo of Liam, senior systems engineer, holding a server handbook"></div>
  <div class="caption" style="left:168px;top:290px"><b>MARCO</b>Support Engineer</div>
  <div class="caption" style="left:326px;top:314px"><b>LIAM</b>Senior Systems<br>Engineer</div>
  <footer class="footer">
    <div class="item"><svg viewBox="0 0 10 8"><path d="M0 0h10v8H0z M0 0l5 4 5-4" stroke="#7d9a3d" stroke-width=".8"/></svg><span>info@brovexa.com.au<br>support@brovexa.com.au</span></div>
    <div class="item"><svg viewBox="0 0 10 10"><path d="M1 2c0-1 1-2 2-2l1 3-1 1c1 2 2 3 4 4l1-1 3 1c0 1-1 2-2 2C5 10 0 5 1 2z"/></svg><span>1300 55 20 47<br>+61 3 9055 2710</span></div>
    <div class="item"><svg viewBox="0 0 10 12"><path d="M5 0a4 4 0 0 1 4 4c0 3-4 8-4 8S1 7 1 4a4 4 0 0 1 4-4z"/></svg><span>Lvl 9/218 Harlow St<br>Melbourne VIC 3000 Australia</span></div>
  </footer>
</section>

<section class="page p-about">
  <div class="abs about-side"></div>
  <div class="abs about-title">ABOUT US</div>
  <div class="side-label" style="top:134px"><svg viewBox="0 0 20 20"><path d="M11 1 5 11h5l-2 8 7-11h-5z" stroke="none"/></svg>OUR PHILOSOPHY</div>
  <div class="side-label" style="top:262px"><svg viewBox="0 0 20 20"><path d="M5 2h10v5a5 5 0 0 1-10 0z M9 12h2v3h3v3H6v-3h3z M5 3H2c0 3 1 5 3 5 M15 3h3c0 3-1 5-3 5" fill="#fff" stroke-width="1.2"/></svg>OUR SUCCESS</div>
  <div class="side-label" style="top:418px"><svg viewBox="0 0 20 20"><circle cx="10" cy="10" r="8.5" fill="none" stroke-width="1.4"/><circle cx="7" cy="8" r="1" stroke="none"/><circle cx="13" cy="8" r="1" stroke="none"/><path d="M6 12c2 3 6 3 8 0" fill="none" stroke-width="1.4"/></svg>OUR DIRECTOR</div>

  <p class="abs about-text" style="top:20px">Everything we do is focused on providing real, measurable benefits to your organisation by improving reliability, performance and collaborating strategically with you to implement enhancements to existing systems and processes.<br>As a Nimbus Silver Small and Midmarket Cloud Solutions Partner and Nimbus Small Business Specialist, Brovexa supports and configures IT systems for small to medium businesses using Nimbus technologies.</p>
  <div class="rule" style="top:98px"></div>
  <p class="abs about-text" style="top:110px">Since our beginnings in 2006, the Brovexa philosophy has always been: "We are a Customer Service Company that just happens to fix IT Systems". This remains our philosophy today, and is Owner &amp; Director Daniel Whitford's favourite saying about how we serve our customers today.<br>Other companies have tried to mirror the Brovexa model (but many have failed):<br>• Fixed Monthly Pricing &nbsp;• 5 Minute Response Guarantee<br>• 24/7 &amp; 365 days support</p>
  <div class="rule" style="top:196px"></div>
  <p class="abs about-text" style="top:204px">The secret to Brovexa's success? Our staff!<br>At Brovexa, we give our staff the freedom to be themselves. Not only are all staff technically trained, they are the forefront of our customer service.<br>We are not happy until the customer is happy!<br>We are very proud of the staff we employ at Brovexa and it's our staff that sets us apart from our peers. Our staff come from varying experience but they all have the one thing in common and that is service.<br>We are simply not happy until the client is happy.<br>When recruiting we look for personalities that match are ethos which is to provide the level of service we would expect if we were the client.<br>All staff are required to maintain and attain industry qualifications, but qualification is only one part of the equation, experience is necessary as well.<br>We ensure that all staff have a minimum of 3 years experience in IT.</p>
  <div class="rule" style="top:356px"></div>
  <p class="abs about-text" style="top:364px">Daniel Whitford setup Brovexa Consulting Services to provide unmatched IT service/support at a True Fixed Monthly Cost. Brovexa has redesigned the landscape of IT support for SME's in Australia by truly providing a new level of service that has not been seen before.</p>
  <p class="abs about-text" style="top:408px">We are constantly setting new trends and goals and is further demonstrated by being one of the first IT providers in Australia truly providing a fixed fee model rather than the typical ad-hoc packages.</p>
  <p class="abs about-text" style="top:444px">Daniel Whitford has over 14 years experience in the IT industry having worked in Melbourne, London, New York, Chicago, San Francisco and Luxembourg. His corporate IT background is extensive having worked for Halden Systems, Meridian News, Harbourline Logistics, Kestrel Investment Group as well as numerous other companies. Daniel understands the critical nature of IT infrastructure and the demand of technical and proactive support to maintain maximum uptime.</p>
  <footer class="footer">
    <div class="item"><svg viewBox="0 0 10 8"><path d="M0 0h10v8H0z M0 0l5 4 5-4" stroke="#7d9a3d" stroke-width=".8"/></svg><span>info@brovexa.com.au<br>support@brovexa.com.au</span></div>
    <div class="item"><svg viewBox="0 0 10 10"><path d="M1 2c0-1 1-2 2-2l1 3-1 1c1 2 2 3 4 4l1-1 3 1c0 1-1 2-2 2C5 10 0 5 1 2z"/></svg><span>1300 55 20 47<br>+61 3 9055 2710</span></div>
    <div class="item"><svg viewBox="0 0 10 12"><path d="M5 0a4 4 0 0 1 4 4c0 3-4 8-4 8S1 7 1 4a4 4 0 0 1 4-4z"/></svg><span>Lvl 9/218 Harlow St<br>Melbourne VIC 3000 Australia</span></div>
  </footer>
</section>

<section class="page p-services">
  <div class="tab">WHAT WE DO</div>
  <div class="abs svc-side"></div>
  <div class="svc-label" style="top:48px">IT SUPPORT<br>SERVICES</div>
  <div class="svc-label" style="top:98px">MANAGED IT<br>SUPPORT<br>SERVICES</div>
  <div class="svc-label" style="top:166px">MANAGED<br>SECURITY</div>
  <div class="svc-label" style="top:240px">ONLINE SYSTEM<br>BACKUPS</div>
  <div class="svc-label" style="top:310px">INTERNET<br>MONITORING</div>
  <div class="svc-label" style="top:371px">CLOUDDESK SUITE</div>
  <div class="svc-label" style="top:415px">IT AUDIT</div>
  <div class="svc-label" style="top:461px">PENETRATION<br>TESTING</div>

  <p class="svc-text" style="top:40px">Imagine if your entire IT environment was monitored <b>24 hours, 7 days</b> a week, <b>365 days</b> a year with problems <b>proactively detected</b> and <b>fixed</b> before they caused any downtime for your business? And now imagine <b>unlimited IT support</b> in Melbourne that is only a phone call away.</p>
  <p class="svc-text" style="top:92px">Brovexa is a leading Managed IT Services provider for organisations requiring consistent high quality, <b>24/7/365 pro-active</b> support based in Melbourne.<br>Why Melbourne businesses choose Brovexa? Our <b>24/7/365</b> remote support is provided by highly skilled engineers with a strong sense of customer services.</p>
  <p class="svc-text" style="top:158px">Cybercrime is on the rise, Brovexa has the experience to protect your infrastructure <b>24/7.</b><br>Cybercrime is increasing, faced with more attacks, business reputations are on the line. Prevention as they say is better than cure, having Brovexa on your side ensures that you have a qualified security team protecting your network 24x7.</p>
  <p class="svc-text" style="top:214px">Never lose data or systems, ever again!<br>Having a backup is vital to ensure business up-time. One strategy that Brovexa recommends is an online backup.<br>Avoiding business disruption following a server failure is one of the biggest business continuity challenges companies face. The legendary reliability of VaultGuard Server provides fast and reliable backup, disaster recovery, enterprise level data protection, and managed system migration to get servers online as quickly as possible after a disaster.</p>
  <p class="svc-text" style="top:302px">Everything, connected.<br>It's about time that network visibility and control was made this simple.<br>• Cloud based<br>• Improve Application Performance</p>
  <p class="svc-text" style="top:354px">Everything, connected. Until recently the benefits of operating a secure and highly available Nimbus Exchange platform were reserved for organisations with substantial monetary and dedicated IT resources, thus putting small and medium sized organisations at a disadvantage. Brovexa together with Nimbus present CloudDesk Suite.</p>
  <p class="svc-text" style="top:408px">Don't spend a fortune on IT auditing services - get our help for free!<br>• Free IT Audit &nbsp;• Work together seamlessly &nbsp;• What our Free IT Audit provides &nbsp;• The Process</p>
  <p class="svc-text" style="top:442px">If there's one powerful way of testing your IT system's security, it's penetration testing. This involves simulating an attack and finding out whether or not your IT system can withstand it. Here at Brovexa Consulting Services, we provide state-of-the-art penetration testing, conducted by a highly-qualified, experienced team. We're pleased to say that we've used this service to help many businesses improve their IT security, thereby saving them a lot of money and stress.</p>
  <footer class="footer">
    <div class="item"><svg viewBox="0 0 10 8"><path d="M0 0h10v8H0z M0 0l5 4 5-4" stroke="#7d9a3d" stroke-width=".8"/></svg><span>info@brovexa.com.au<br>support@brovexa.com.au</span></div>
    <div class="item"><svg viewBox="0 0 10 10"><path d="M1 2c0-1 1-2 2-2l1 3-1 1c1 2 2 3 4 4l1-1 3 1c0 1-1 2-2 2C5 10 0 5 1 2z"/></svg><span>1300 55 20 47<br>+61 3 9055 2710</span></div>
    <div class="item"><svg viewBox="0 0 10 12"><path d="M5 0a4 4 0 0 1 4 4c0 3-4 8-4 8S1 7 1 4a4 4 0 0 1 4-4z"/></svg><span>Lvl 9/218 Harlow St<br>Melbourne VIC 3000 Australia</span></div>
  </footer>
</section>

<section class="page p-values">
  <div class="tab">OUR VALUES</div>
  <div class="abs values-art" role="img" aria-label="Illustrated team values poster with hand lettered pledges: we take initiative, we have empathy not egos, we are relentless, we respect, set among playful green and yellow shapes"></div>
  <div class="abs values-bottom"></div>
  <div class="tab tab-test">TESTIMONIAL</div>
  <div class="bubble" style="left:22px;top:372px;width:134px;height:136px">Calloway bakers have been long standing customers of Brovexa for over 5 years now. I trust Brovexa with the IT issues for more than 15 PC's and a server for our medium size business. Everything we throw at the team is resolved with skill and knowledge in a timely fashion.</div>
  <div class="person" style="left:160px;top:472px"><b>Peter Calloway</b><br>(Calloway Bakers)</div>
  <div class="bubble" style="left:244px;top:396px;width:140px;height:116px">We have been with Brovexa for approximately 5 years now. During this time they have quite professionally lead us through a number of infrastructure changes. I have no hesitation whatsoever to recommend their services to any prospective customers.</div>
  <div class="person" style="left:182px;top:514px"><b>Samuel Reyes</b><br>(Coastal Insurance Group)</div>
</section>

</body>
</html>
```